Create Direct Mail Flyer For House Painting Company

The flyer needs to promote "Free Cheese Every Month" (When they paint their whole house. We want to Focus on the offer, also a free colour consultation, the awards and the guarantees! This will be a full colour 2 sided letter box drop flyer.
This is an emotional Direct Response flyer. I want the Headline to be Bold and stand out. Follow the branding if the website https://larkfieldresidencecraft.com.au/
I have attached some social media photos to show you the promotion idea of free cheese every month. Use better photos if you have them.
I have given you a number of photos to use on the brochure, use your skills to determine what you feel is best to use. Also with the Colour consultation points use small photos to emphasise the points.
Have the testimonials and the team photo on the back.
Also have urgency. ACT NOW -OFFER ENDING SOON!

Target Market(s)

Home Owners

Industry/Entity Type

House Painting, Roof Painting

Colors
0054AA
0677BA
7BADD7
CADEEF
E8F1F8

Requirements
Must have
• Keep the Brand Colours. I have attached a sample flyer that shows a concept that I like. Have the testimonials on the back of the flyer. I do not want the flyer to look to busy.

```html
<!DOCTYPE html>
<html lang="en">
<head>
<meta charset="utf-8">
<title>Larkfield Residence Craft – Free Cheese Every Month</title>
<link href="https://fonts.googleapis.com/css2?family=Oswald:wght@500;600;700&family=Montserrat:wght@700;800&family=Open+Sans:ital,wght@0,400;0,600;0,700;1,400&display=swap" rel="stylesheet">
<style>
:root{
  --brand-deep:#0054AA;
  --brand:#0677BA;
  --brand-mid:#7BADD7;
  --brand-pale:#CADEEF;
  --brand-mist:#E8F1F8;
  --plum-dark:#2e1232;
  --plum:#5a1f4f;
  --gold:#f6d36b;
  --ring:#d9b25a;
  --ink:#1d2a3a;
  --tick:#4caf3f;
  --sage:#f0f4ec;
  --star:#f2b01e;
  --white:#ffffff;
}
*{box-sizing:border-box;margin:0;padding:0}
html,body{width:1200px;height:3480px;overflow:hidden;background:var(--white)}
body{font-family:"Open Sans",Arial,sans-serif;color:var(--ink);position:relative}
.abs{position:absolute}
.condensed{font-family:"Oswald","Arial Narrow",sans-serif}

/* Front header */
.hero{left:0;top:0;width:1200px;height:768px;background:linear-gradient(160deg,var(--plum) 0%,var(--plum-dark) 70%)}
.hero-photo{left:720px;top:230px;width:480px;height:538px;background:radial-gradient(circle at 55% 45%,#b5343f 0%,#6d1a2a 45%,#2e1232 85%)}
.hero-title{left:0;top:26px;width:1200px;text-align:center;color:var(--white);white-space:nowrap}
.hero-title .lead{font-size:58px;font-weight:600;line-height:1.15}
.hero-title .offer{font-size:94px;font-weight:700;color:var(--gold);line-height:1.2}
.hero-copy{left:60px;top:234px;width:650px;color:var(--white);font-size:22px;line-height:1.4}
.hero-copy b{color:var(--gold)}
.logo-disc{left:28px;top:410px;width:246px;height:246px;border-radius:50%;background:var(--white);display:flex;align-items:center;justify-content:center;text-align:center}
.logo-disc .name{font-family:"Montserrat",Arial,sans-serif;font-weight:800;font-size:25px;color:var(--brand-deep);line-height:1.2}
.seal{border-radius:50%;background:radial-gradient(circle,var(--brand) 0%,var(--brand-deep) 100%);border:6px solid var(--ring);display:flex;align-items:center;justify-content:center;text-align:center;color:var(--white);font-family:"Montserrat",Arial,sans-serif;font-weight:800}
.seal-award{left:292px;top:420px;width:230px;height:230px;font-size:27px;line-height:1.2}
.seal-colour{left:512px;top:398px;width:190px;height:190px;font-size:24px;line-height:1.2}

/* Steps */
.steps-band{left:0;top:768px;width:1200px;height:172px;background:var(--brand-deep);color:var(--white);text-align:center;padding-top:30px}
.steps-band h2{font-size:48px;font-weight:600;line-height:1.2}
.steps-band p{font-size:32px;font-weight:500;margin-top:4px}
.steps{left:0;top:940px;width:1200px;height:1120px;background:var(--brand-mist)}
.step{position:absolute;left:40px;width:1120px;height:250px;display:flex;gap:36px;align-items:center}
.step-photo{width:300px;height:236px;flex:none;border:3px solid var(--white)}
.step-text{border-left:4px solid var(--brand);padding-left:24px}
.step-text h3{font-family:"Montserrat",Arial,sans-serif;font-size:28px;font-weight:700;color:var(--brand-deep);margin-bottom:8px}
.step-text p{font-size:20px;line-height:1.45}
.ph-mood{background:linear-gradient(135deg,#2d4f7c,#9fb8d4)}
.ph-light{background:linear-gradient(135deg,#f1f3f5,#7c9bbd)}
.ph-function{background:linear-gradient(135deg,#1e3a5f,#c9d6e4)}
.ph-test{background:linear-gradient(135deg,#7a8ea6,#e7edf3)}

/* Back */
.back-head{left:0;top:2100px;width:1200px;height:280px;background:linear-gradient(180deg,rgba(0,84,170,.72),rgba(0,84,170,.88)),linear-gradient(120deg,#7b8ea3,#c6d3de);display:flex;align-items:center;justify-content:center}
.back-head h2{color:var(--white);font-size:52px;font-weight:600;text-align:center;line-height:1.2;white-space:nowrap}
.assure{left:0;top:2380px;width:1200px;height:262px;background:var(--sage)}
.check-list{list-style:none;position:absolute;top:38px}
.check-list li{display:flex;align-items:center;gap:14px;font-size:21px;font-weight:600;height:46px;white-space:nowrap}
.tick{width:28px;height:28px;flex:none}
.guarantees{left:40px}
.services{left:520px;top:30px}
.services h3{font-size:22px;font-weight:700;color:var(--ink);margin-bottom:4px}
.badge{width:280px;height:80px;border-radius:6px;background:linear-gradient(90deg,#3a3a3a 0 36%,#cfcfcf 36%)}
.praise-title{left:0;top:2654px;width:1200px;text-align:center;font-family:"Montserrat",Arial,sans-serif;font-size:32px;font-weight:800;color:var(--brand-deep)}
.review{position:absolute;width:540px}
.stars{display:flex;gap:4px;margin-bottom:6px}
.stars svg{width:28px;height:28px}
.review p{font-size:16px;line-height:1.42;font-style:italic}
.review .who{font-style:normal;margin-top:4px}
.cta{left:0;top:3070px;width:1200px;text-align:center}
.cta h3{font-size:30px;font-weight:600;color:var(--brand-deep);white-space:nowrap}
.cta p{font-size:22px;font-weight:700;color:var(--brand-deep);margin-top:6px}
.team-photo{left:0;top:3190px;width:1200px;height:290px;background:linear-gradient(180deg,#8fb4d8 0%,#3f5f82 60%,#22374f 100%)}
.team-logo{left:60px;top:3240px;width:250px;height:180px;border-radius:10px;background:var(--white);display:flex;align-items:center;justify-content:center;text-align:center}
.team-logo span{font-family:"Montserrat",Arial,sans-serif;font-weight:800;font-size:26px;color:var(--brand-deep);line-height:1.2}
</style>
</head>
<body>

<section class="abs hero">
  <div class="abs hero-photo" role="img" aria-label="Photo of a cheese platter beside a freshly painted wall"></div>
  <div class="abs hero-title condensed">
    <h1 class="lead">Transform Your Home and Sip on</h1>
    <div class="offer">Free Cheese Every Month!</div>
  </div>
  <p class="abs hero-copy">Paint your whole house with us and receive a <b>FREE COLOUR CONSULTATION</b> to ensure the perfect shade. Plus, enjoy free cheese every month, on us. Our skilled painters are ready to transform your home.</p>
  <div class="abs logo-disc"><span class="name">Larkfield<br>Residence Craft</span></div>
  <div class="abs seal seal-award">Award-<br>Winning<br>Services You<br>Can Trust</div>
  <div class="abs seal seal-colour">Free<br>Colour<br>Consultation</div>
</section>

<section class="abs steps-band condensed">
  <h2>Four Steps to Bring Your Vision to Life!</h2>
  <p>It is important to select the correct colours for your home.</p>
</section>

<section class="abs steps">
  <div class="step" style="top:20px">
    <div class="step-photo ph-mood" role="img" aria-label="Photo of a calm blue living room"></div>
    <div class="step-text"><h3>1. Consider the mood you want to create:</h3>
    <p>Think about the atmosphere you want to evoke in each room. Do you want a calming and relaxing space, or a vibrant and energizing one? Choose colours that align with the mood you want to create.</p></div>
  </div>
  <div class="step" style="top:295px">
    <div class="step-photo ph-light" role="img" aria-label="Photo of a bright room with large windows"></div>
    <div class="step-text"><h3>2. Look at the room's natural light:</h3>
    <p>Take note of the amount and direction of natural light each room gets. Light affects how colours appear, so you'll want to choose shades that complement the lighting. For example, warm hues like red and orange work well in rooms with a lot of natural light, while cool hues like blue and green are better suited for rooms with less light.</p></div>
  </div>
  <div class="step" style="top:570px">
    <div class="step-photo ph-function" role="img" aria-label="Photo of a navy bedroom"></div>
    <div class="step-text"><h3>3. Think about the room's function:</h3>
    <p>Consider the purpose of each room and choose colours that align with the function. For instance, blue or green may be suitable for a bedroom to create a calming environment, while yellow or orange may work well in a kitchen to add warmth and energy.</p></div>
  </div>
  <div class="step" style="top:845px">
    <div class="step-photo ph-test" role="img" aria-label="Photo of paint swatches tested on a wall"></div>
    <div class="step-text"><h3>4. Test the colours:</h3>
    <p>Once you've narrowed down your choices, test them out in the room. Paint a small patch on the wall and observe how it looks at different times of the day and in different lighting conditions. This will help you determine if the colour is right for the space.</p></div>
  </div>
</section>

<section class="abs back-head" role="img" aria-label="Faded photo of a painted house exterior">
  <h2 class="condensed">Rest Assured with Our Guaranteed Professional Services:</h2>
</section>

<section class="abs assure">
  <ul class="check-list guarantees">
    <li><svg class="tick" viewBox="0 0 30 30"><circle cx="15" cy="15" r="15" fill="var(--tick)"/><path d="M8 15.5l4.5 4.5L22 10.5" stroke="#fff" stroke-width="3.4" fill="none" stroke-linecap="round" stroke-linejoin="round"/></svg>On Time Guarantee</li>
    <li><svg class="tick" viewBox="0 0 30 30"><circle cx="15" cy="15" r="15" fill="var(--tick)"/><path d="M8 15.5l4.5 4.5L22 10.5" stroke="#fff" stroke-width="3.4" fill="none" stroke-linecap="round" stroke-linejoin="round"/></svg>White Glove Cleanliness Guarantee</li>
    <li><svg class="tick" viewBox="0 0 30 30"><circle cx="15" cy="15" r="15" fill="var(--tick)"/><path d="M8 15.5l4.5 4.5L22 10.5" stroke="#fff" stroke-width="3.4" fill="none" stroke-linecap="round" stroke-linejoin="round"/></svg>15 Year Guarantee</li>
    <li><svg class="tick" viewBox="0 0 30 30"><circle cx="15" cy="15" r="15" fill="var(--tick)"/><path d="M8 15.5l4.5 4.5L22 10.5" stroke="#fff" stroke-width="3.4" fill="none" stroke-linecap="round" stroke-linejoin="round"/></svg>Satisfaction Guarantee</li>
  </ul>
  <div class="abs services">
    <h3>Our Range of Services:</h3>
    <ul class="check-list" style="position:static">
      <li><svg class="tick" viewBox="0 0 30 30"><circle cx="15" cy="15" r="15" fill="var(--tick)"/><path d="M8 15.5l4.5 4.5L22 10.5" stroke="#fff" stroke-width="3.4" fill="none" stroke-linecap="round" stroke-linejoin="round"/></svg>Roof Restoration &amp; Painting</li>
      <li><svg class="tick" viewBox="0 0 30 30"><circle cx="15" cy="15" r="15" fill="var(--tick)"/><path d="M8 15.5l4.5 4.5L22 10.5" stroke="#fff" stroke-width="3.4" fill="none" stroke-linecap="round" stroke-linejoin="round"/></svg>House Painting</li>
      <li><svg class="tick" viewBox="0 0 30 30"><circle cx="15" cy="15" r="15" fill="var(--tick)"/><path d="M8 15.5l4.5 4.5L22 10.5" stroke="#fff" stroke-width="3.4" fill="none" stroke-linecap="round" stroke-linejoin="round"/></svg>Epoxy Floors</li>
    </ul>
  </div>
  <div class="abs badge" style="left:890px;top:40px"></div>
  <div class="abs badge" style="left:890px;top:140px"></div>
</section>

<h2 class="abs praise-title">Happy Customers Speak:</h2>

<div class="review" style="left:40px;top:2706px">
  <div class="stars"><svg viewBox="0 0 24 24"><path fill="var(--star)" d="M12 2l3 6.5 7 .8-5.2 4.8 1.4 7L12 17.6 5.8 21.1l1.4-7L2 9.3l7-.8z"/></svg><svg viewBox="0 0 24 24"><path fill="var(--star)" d="M12 2l3 6.5 7 .8-5.2 4.8 1.4 7L12 17.6 5.8 21.1l1.4-7L2 9.3l7-.8z"/></svg><svg viewBox="0 0 24 24"><path fill="var(--star)" d="M12 2l3 6.5 7 .8-5.2 4.8 1.4 7L12 17.6 5.8 21.1l1.4-7L2 9.3l7-.8z"/></svg><svg viewBox="0 0 24 24"><path fill="var(--star)" d="M12 2l3 6.5 7 .8-5.2 4.8 1.4 7L12 17.6 5.8 21.1l1.4-7L2 9.3l7-.8z"/></svg><svg viewBox="0 0 24 24"><path fill="var(--star)" d="M12 2l3 6.5 7 .8-5.2 4.8 1.4 7L12 17.6 5.8 21.1l1.4-7L2 9.3l7-.8z"/></svg></div>
  <p>"Most professional painters we have ever dealt with from precision of work, tidiness, promptness, reliable company that followed up all queries immediately and with politeness at all times."</p>
  <p class="who">- Bronwen Van Dalen</p>
</div>
<div class="review" style="left:40px;top:2856px">
  <div class="stars"><svg viewBox="0 0 24 24"><path fill="var(--star)" d="M12 2l3 6.5 7 .8-5.2 4.8 1.4 7L12 17.6 5.8 21.1l1.4-7L2 9.3l7-.8z"/></svg><svg viewBox="0 0 24 24"><path fill="var(--star)" d="M12 2l3 6.5 7 .8-5.2 4.8 1.4 7L12 17.6 5.8 21.1l1.4-7L2 9.3l7-.8z"/></svg><svg viewBox="0 0 24 24"><path fill="var(--star)" d="M12 2l3 6.5 7 .8-5.2 4.8 1.4 7L12 17.6 5.8 21.1l1.4-7L2 9.3l7-.8z"/></svg><svg viewBox="0 0 24 24"><path fill="var(--star)" d="M12 2l3 6.5 7 .8-5.2 4.8 1.4 7L12 17.6 5.8 21.1l1.4-7L2 9.3l7-.8z"/></svg><svg viewBox="0 0 24 24"><path fill="var(--star)" d="M12 2l3 6.5 7 .8-5.2 4.8 1.4 7L12 17.6 5.8 21.1l1.4-7L2 9.3l7-.8z"/></svg></div>
  <p>"Repaired and sealed my tile roof and repainted my water stained ceilings. Fast quote, fast turnaround on the job. Great team, trustworthy with full access to my home while I was at work. Cheaper quote but wore a 15 year Coloria guarantee on the work. Can certainly recommend."</p>
  <p class="who">- Diana K</p>
</div>
<div class="review" style="left:620px;top:2706px">
  <div class="stars"><svg viewBox="0 0 24 24"><path fill="var(--star)" d="M12 2l3 6.5 7 .8-5.2 4.8 1.4 7L12 17.6 5.8 21.1l1.4-7L2 9.3l7-.8z"/></svg><svg viewBox="0 0 24 24"><path fill="var(--star)" d="M12 2l3 6.5 7 .8-5.2 4.8 1.4 7L12 17.6 5.8 21.1l1.4-7L2 9.3l7-.8z"/></svg><svg viewBox="0 0 24 24"><path fill="var(--star)" d="M12 2l3 6.5 7 .8-5.2 4.8 1.4 7L12 17.6 5.8 21.1l1.4-7L2 9.3l7-.8z"/></svg><svg viewBox="0 0 24 24"><path fill="var(--star)" d="M12 2l3 6.5 7 .8-5.2 4.8 1.4 7L12 17.6 5.8 21.1l1.4-7L2 9.3l7-.8z"/></svg><svg viewBox="0 0 24 24"><path fill="var(--star)" d="M12 2l3 6.5 7 .8-5.2 4.8 1.4 7L12 17.6 5.8 21.1l1.4-7L2 9.3l7-.8z"/></svg></div>
  <p>"Daniel Barrow and his team are true professionals. Daniel sent his A team lead by Harper to paint the interior and exterior of our new build. The attention to detail is exceptional, best paint team I have ever used. I would not hesitate to use them on all our future projects."</p>
  <p class="who">- Glen Vance</p>
</div>
<div class="review" style="left:620px;top:2896px">
  <div class="stars"><svg viewBox="0 0 24 24"><path fill="var(--star)" d="M12 2l3 6.5 7 .8-5.2 4.8 1.4 7L12 17.6 5.8 21.1l1.4-7L2 9.3l7-.8z"/></svg><svg viewBox="0 0 24 24"><path fill="var(--star)" d="M12 2l3 6.5 7 .8-5.2 4.8 1.4 7L12 17.6 5.8 21.1l1.4-7L2 9.3l7-.8z"/></svg><svg viewBox="0 0 24 24"><path fill="var(--star)" d="M12 2l3 6.5 7 .8-5.2 4.8 1.4 7L12 17.6 5.8 21.1l1.4-7L2 9.3l7-.8z"/></svg><svg viewBox="0 0 24 24"><path fill="var(--star)" d="M12 2l3 6.5 7 .8-5.2 4.8 1.4 7L12 17.6 5.8 21.1l1.4-7L2 9.3l7-.8z"/></svg><svg viewBox="0 0 24 24"><path fill="var(--star)" d="M12 2l3 6.5 7 .8-5.2 4.8 1.4 7L12 17.6 5.8 21.1l1.4-7L2 9.3l7-.8z"/></svg></div>
  <p>"Recently had the exterior of my home and deck painted. The painters who came were very professional and friendly. Would not hesitate to recommend them for any painting requirements you might have."</p>
  <p class="who">- Sal Chandler</p>
</div>

<div class="abs cta">
  <h3 class="condensed">Grab Your Free Cheese &amp; Colour Consultation While this Offer Lasts. Call Us Today!</h3>
  <p>1300 555 019 • admin@larkfieldresidencecraft.com.au • larkfieldresidencecraft.com.au</p>
</div>

<div class="abs team-photo" role="img" aria-label="Team photo of the painting crew in front of their branded vans"></div>
<div class="abs team-logo"><span>Larkfield<br>Residence Craft</span></div>

</body>
</html>
```